Website design for recruitment solutions

We connect top talents to fast growing employers in Asia. We need to revamp our existing website (currently outdated) and also add more pages to make it more informative for talents and employers.
We need final design output to be for both desktop and mobile devices. The final design output must come with all specifications so it's easier for our dev team to implement. We have a detailed mockup but we expect the design to be significantly changed by the final output. We want the pages to look aesthetic, modern and professional.
Number of Pages Required
5+ page
Requirements
Must have
- - To have Pages design for desktop+mobile. Need to take into account intermediate resolutions like 1365px\1023px\767px\479px, especially if mobile/desktop design differs considerably. Design should be repeatable (between pages), suitable for block-layout.
Nice to have
- In terms of receiving files, we usually work with designers who can deliver files in Figma or Sketch with export to Figma. If in PSD format - please export to Zeplin or Avocode, otherwise will be difficult to open

```html
<!DOCTYPE html>
<html lang="en">
<head>
<meta charset="utf-8">
<title>HIRELINK – Recruitment</title>
<link href="https://fonts.googleapis.com/css2?family=Nunito+Sans:wght@300;400;600;700&display=swap" rel="stylesheet">
<style>
:root{
  --red:#ee1111;
  --navy:#3e5a89;
  --navy-dark:#375181;
  --heading-blue:#3b5b8f;
  --green:#5bc38a;
  --text-grey:#555a60;
  --white:#ffffff;
  --wave-line:#b8c4d8;
}
*{margin:0;padding:0;box-sizing:border-box}
html,body{width:1200px;height:2805px;overflow:hidden}
body{position:relative;font-family:'Nunito Sans',sans-serif;background:var(--white);color:var(--text-grey)}
.abs{position:absolute}

/* Hero */
.hero{position:absolute;left:0;top:0;width:1200px;height:730px}
.hero-photo{position:absolute;inset:0;background:radial-gradient(ellipse at 55% 30%,#7a7470 0%,#4a4c52 40%,#2c3440 75%,#1f2833 100%)}
.logo{left:63px;top:34px;font-size:38px;font-weight:600;color:var(--white);letter-spacing:.5px}
.nav{left:396px;top:45px;display:flex;gap:37px;font-size:15px;color:var(--white);font-weight:400}
.btn-register{left:936px;top:33px;width:110px;height:41px;background:var(--red);color:var(--white);font-size:14px;display:flex;align-items:center;justify-content:center}
.btn-login{left:1053px;top:33px;width:110px;height:41px;border:2px solid var(--white);color:var(--white);font-size:14px;display:flex;align-items:center;justify-content:center}
.hero-title{left:0;top:280px;width:1200px;text-align:center;color:var(--white);font-size:41px;font-weight:600;line-height:49px}
.btn-start{left:497px;top:394px;width:206px;height:56px;background:var(--red);color:var(--white);font-size:23px;font-weight:600;display:flex;align-items:center;justify-content:center}
.learn-more{left:0;top:586px;width:1200px;text-align:center;color:var(--white);font-size:22px;font-weight:600}

/* Smart connections */
.dashboard-image{left:116px;top:812px;width:474px;height:384px;border-radius:10px;background:linear-gradient(160deg,#eef1f6 0%,#d9dde6 55%,#b9bcc4 100%)}
.section-title{font-size:36px;font-weight:600;line-height:44px}
.smart-title{left:662px;top:868px;color:#3a3d42}
.smart-text{left:663px;top:932px;width:470px;font-size:20px;line-height:34px;color:#4a4e54}

/* Critical insights */
.insights-title{left:125px;top:1402px;color:var(--white)}
.insights-text{left:126px;top:1466px;width:480px;font-size:20px;line-height:34px;color:var(--white)}
.globe{left:650px;top:1323px;width:436px;height:436px;border-radius:50%;background:radial-gradient(circle at 60% 45%,#6fa4d8 0%,#2a5a9a 35%,#0f2a52 70%,#05101f 100%)}

/* People first */
.people-title{left:0;top:1888px;width:1200px;text-align:center;color:var(--heading-blue);font-size:32px;font-weight:600}
.people-text{left:150px;top:1936px;width:900px;text-align:center;font-size:17px;line-height:30px;color:#4a4e54}
.card{left:306px;top:2045px;width:603px;height:290px;background:var(--white);box-shadow:0 2px 12px rgba(0,0,0,.12)}
.quote-badge{left:272px;top:30px;width:56px;height:56px;border-radius:50%;background:var(--green);color:var(--white);font-size:52px;font-weight:700;line-height:72px;text-align:center}
.quote-text{left:0;top:103px;width:603px;text-align:center;font-size:18px;line-height:28px;color:#5a5e64;font-weight:300}
.quote-rule{left:278px;top:195px;width:46px;height:3px;background:var(--red)}
.quote-author{left:0;top:215px;width:603px;text-align:center;font-size:19px;font-weight:600;color:#3a3d42}

/* Footer */
.footer{left:0;top:2415px;width:1200px;height:390px;background:var(--navy)}
.footer-bar{left:0;top:2723px;width:1200px;height:82px;background:var(--navy-dark)}
.footer-logo{left:110px;top:2490px;font-size:27px;font-weight:600;color:var(--white)}
.footer-about{left:110px;top:2535px;width:290px;font-size:12px;line-height:23px;color:var(--white)}
.col-title{font-size:17px;font-weight:600;color:var(--white)}
.col-link{font-size:16px;color:#e6ebf3}
.footer-register{left:481px;top:2592px;width:111px;height:36px;background:var(--red);color:var(--white);font-size:15px;display:flex;align-items:center;justify-content:center}
.legal{font-size:12px;line-height:15px;color:var(--white)}
</style>
</head>
<body>

<section class="hero">
  <div class="hero-photo" role="img" aria-label="Photo of two businessmen smiling and shaking hands in an office"></div>
  <div class="abs logo">HIRELINK</div>
  <nav class="abs nav"><span>HOW WE WORK</span><span>BROWSE JOBS</span><span>EMPLOYERS</span><span>ABOUT US</span></nav>
  <div class="abs btn-register">REGISTER</div>
  <div class="abs btn-login">LOG IN</div>
  <h1 class="abs hero-title">WE CONNECT TOP TALENTS INTO<br>FAST GROWING EMPLOYERS IN ASIA</h1>
  <div class="abs btn-start">Get Started</div>
  <div class="abs learn-more">Learn More</div>
  <svg class="abs" style="left:0;top:0" width="1200" height="740" viewBox="0 0 1200 740">
    <path d="M0 670 C120 720 300 700 460 672 C540 658 580 650 600 650 C640 650 700 660 800 685 C950 720 1100 700 1200 660 L1200 740 L0 740 Z" fill="#ffffff"/>
    <path d="M170 728 C330 720 470 680 580 662 C640 655 700 668 820 700 C950 730 1080 725 1200 700" fill="none" stroke="var(--wave-line)" stroke-width="3"/>
    <circle cx="601" cy="658" r="21" fill="#3e5a89" stroke="#ffffff" stroke-width="3"/>
    <path d="M593 655 L601 663 L609 655" fill="none" stroke="#ffffff" stroke-width="2.5"/>
  </svg>
</section>

<section>
  <div class="abs dashboard-image" role="img" aria-label="Illustration of a computer showing an analytics dashboard"></div>
  <h2 class="abs section-title smart-title">SMART CONNECTIONS</h2>
  <p class="abs smart-text">It's the quality of the connection that matters. Our role matching algorithms and talent managers work around the clock to find opportunities suitable to your unique profile.</p>
</section>

<section>
  <svg class="abs" style="left:0;top:1275px" width="1200" height="560" viewBox="0 0 1200 560">
    <defs><linearGradient id="band" x1="0" y1="0" x2="1" y2="0.2"><stop offset="0" stop-color="#43618b"/><stop offset="0.5" stop-color="#4f9a86"/><stop offset="1" stop-color="#5bc58a"/></linearGradient></defs>
    <path d="M0 0 H1200 V510 C1120 540 1050 550 960 535 C820 510 700 480 600 488 C440 500 300 560 150 548 C80 543 30 530 0 520 Z" fill="url(#band)"/>
  </svg>
  <h2 class="abs section-title insights-title">CRITICAL INSIGHTS</h2>
  <p class="abs insights-text">Our close interactions with candidates and employers have helped us create a comprehensive database of companies, talents and skills. With HIRELINK, you will gain full access to timely intel to help you make the right career decision.</p>
  <div class="abs globe" role="img" aria-label="Hand reaching toward a glowing digital globe network"></div>
</section>

<section>
  <h2 class="abs people-title">PEOPLE FIRST</h2>
  <p class="abs people-text">We take the time to really understand you holistically as a person to maximize your potential. As your career counselor, we provide maximum transparency and feedback throughout the process.</p>
  <svg class="abs" style="left:128px;top:2162px" width="20" height="36" viewBox="0 0 20 36"><path d="M17 2 L3 18 L17 34" fill="none" stroke="#b5b8bd" stroke-width="3"/></svg>
  <svg class="abs" style="left:1072px;top:2162px" width="20" height="36" viewBox="0 0 20 36"><path d="M3 2 L17 18 L3 34" fill="none" stroke="#b5b8bd" stroke-width="3"/></svg>
  <div class="abs card">
    <div class="abs quote-badge">&ldquo;</div>
    <p class="abs quote-text">Pellentesque faucibus Ut accumsan ultricies elit<br>Maecenas at justo id velit placerat molestie Donec dictum<br>lectus non odio Cras a ante vitae enim</p>
    <div class="abs quote-rule"></div>
    <div class="abs quote-author">By Author Name</div>
  </div>
</section>

<footer>
  <div class="abs footer"></div>
  <svg class="abs" style="left:560px;top:2414px" width="80" height="46" viewBox="0 0 80 46">
    <path d="M0 0 H80 C62 4 56 42 40 42 C24 42 18 4 0 0 Z" fill="#ffffff"/>
    <path d="M40 31 V19 M35 24 L40 19 L45 24" fill="none" stroke="#3e5a89" stroke-width="2"/>
  </svg>
  <div class="abs footer-logo">HIRELINK</div>
  <p class="abs footer-about">Augiat in pede Fusce tellus Sed metus augue convallis et vehicula ut pulvinar eu ante Integer orci tellus tristique vitae consequat nec mauris viverra in gravida eu mattis in ante Morbi eget arcumentum vel congue id euismod in elit Fusce</p>
  <div class="abs col-title" style="left:481px;top:2486px">TALENT</div>
  <div class="abs col-link" style="left:481px;top:2522px">How we work</div>
  <div class="abs col-link" style="left:481px;top:2549px">Browse Jobs</div>
  <div class="abs footer-register">Register</div>
  <div class="abs col-title" style="left:691px;top:2488px">EMPLOYERS</div>
  <div class="abs col-link" style="left:693px;top:2522px">Why HIRELINK</div>
  <div class="abs col-title" style="left:918px;top:2484px">ABOUT US</div>
  <div class="abs col-link" style="left:917px;top:2517px">About HIRELINK</div>
  <div class="abs footer-bar"></div>
  <div class="abs legal" style="left:110px;top:2755px;font-size:13px">Hirelink 2012-2020. All rights reserved</div>
  <div class="abs legal" style="left:481px;top:2738px;width:290px">Northgate Staffing Ltd (EA License No. 40217)<br>Unit 12, Level 5, Harbour Tower B, 88<br>Marina Road, Kowloon, Hong Kong</div>
  <div class="abs legal" style="left:785px;top:2738px;width:380px">Hirelink Pte. Ltd. (License No. 19C4402)<br>45 Palm Avenue, #12-03 Meridian House, Singapore 079120</div>
</footer>

</body>
</html>
```